Dark Comedy Movie Poster

We need a poster design for our short film BRAM that we just wrapped on.
It's a dark comedy
Bram explores the world of loneliness through the lens of a manic man-child. Bram wants nothing more than the approval of others, giving every last bit of energy to the cause. But his ravenous attempts accomplish the opposite, turning others off. His desperation is authentic, his lonliness cavernous.
Here is a link to the film
https://clipvault.example/548207316
Password: Bram42
I want you, the artist, to pitch me an idea in any way you want. I'm open to absolutely anything right now. Once I have some pitches from you all my production team and I will sort through them and pick the best fit!
-Owen

```html
<!DOCTYPE html>
<html lang="en">
<head>
<meta charset="UTF-8">
<title>BRAM — Poster</title>
<link rel="stylesheet" href="https://fonts.googleapis.com/css2?family=Libre+Baskerville:wght@700&family=Tangerine:wght@700&display=swap">
<style>
  :root {
    --ink-white: #ffffff;
    --gold-core: #f2d21a;
    --gold-mid: #d9b321;
    --umber-edge: #7a4a1c;
    --umber-deep: #4d2a12;
    --portrait-light: #f7e37a;
    --portrait-warm: #c9a33a;
    --portrait-shadow: #6b5a20;
    --shirt-violet: #8e78b8;
  }
  * { margin: 0; padding: 0; box-sizing: border-box; }
  html, body { width: 800px; height: 1200px; overflow: hidden; }
  body { background: var(--umber-deep); }

  .poster {
    position: relative;
    width: 800px;
    height: 1200px;
    overflow: hidden;
    background:
      radial-gradient(ellipse 75% 60% at 55% 45%, var(--gold-core) 0%, var(--gold-mid) 55%, var(--umber-edge) 92%, var(--umber-deep) 100%);
    color: var(--ink-white);
  }

  .portrait {
    position: absolute;
    left: 70px;
    top: 350px;
    width: 470px;
    height: 850px;
    border-radius: 48% 48% 0 0 / 30% 30% 0 0;
    background:
      linear-gradient(180deg, var(--portrait-shadow) 0%, var(--portrait-warm) 16%, var(--portrait-light) 40%, var(--portrait-warm) 70%, var(--shirt-violet) 100%);
    opacity: 0.85;
  }

  .title {
    position: absolute;
    top: 40px;
    left: 0;
    width: 100%;
    text-align: center;
    font-family: "Libre Baskerville", serif;
    font-weight: 700;
    font-size: 198px;
    line-height: 1;
    letter-spacing: 4px;
  }

  .tagline {
    position: absolute;
    left: 160px;
    top: 228px;
    font-family: "Tangerine", cursive;
    font-weight: 700;
    font-size: 118px;
    line-height: 1;
  }

  .tagline-sub {
    position: absolute;
    left: 408px;
    top: 330px;
    font-family: "Libre Baskerville", serif;
    font-weight: 700;
    font-size: 30px;
    line-height: 1;
  }

  .footer {
    position: absolute;
    left: 0;
    bottom: 44px;
    width: 100%;
    text-align: center;
    font-family: "Libre Baskerville", serif;
    font-weight: 700;
    line-height: 1;
  }
  .footer-main { display: block; font-size: 78px; letter-spacing: 1px; }
  .footer-sub { display: block; font-size: 44px; margin-top: 4px; letter-spacing: 1px; }
</style>
</head>
<body>
  <main class="poster">
    <div class="portrait" role="img" aria-label="Painted portrait of Bram looking upward, warm yellow tones, lavender shirt"></div>
    <h1 class="title">BRAM</h1>
    <p class="tagline">Accomplished</p>
    <p class="tagline-sub">all his goals</p>
    <p class="footer">
      <span class="footer-main">ALL OF THEM</span>
      <span class="footer-sub">EVERY...SINGLE..ONE!!!</span>
    </p>
  </main>
</body>
</html>
```